Stylish Design With Simple UI For Appointment Site

Note: Logo file now attached. Extra credit to anyone who offers basic HTML templates in the final deliverable, incorporating the individual components of the design (using DIVs and CSS).

There are two key requirements for this site:

1. It makes our site look like one of the most professional of its kind. We want to look the part;
2. It has a very simple, straight-forward user interface. We're nothing without being intuitive.

Our site will be used by other businesses to set up their own online booking systems.

Logo samples attached. The colour scheme is not yet set but two possible options are:

1. Dark (#323B3A) & Blue (#12B5D4) on White background
2. White & Yellow (#FEF102) on Grey (#3A3A3C) background

For inspiration, and an idea of what we like, take a look at quillbarn.com - it's very clear and eye-catching, although its pages are longer than we would like ours to be. Oh but we don't need a chimp! Instead of the section with the chimp in, we would like a changing image headline section on the home page, in the style of fellgarde.co.uk (with a less high image; we have attached one image which you may want to try out with this, but happy to see other ideas).

Any graphics included must be royalty free and free for commercial use. Fonts should be readily available and specified.

We would like to see the design applied to the following pages:

1. The main public home page (features header, login prompt, menu, changing image banner with headlines, main body, footer menu).
2. A secondary public page (features a similar layout to home page but without image headline banner, includes extra panels/body detail).
3. The Control Panel page (features several list panels and an add appointment button).
4. A list-style administration page (with popup item editor window).
5. A settings administration page (with form).

In that order, a sample walk-through design spec will be attached.

To summarise, we are looking for someone to put forward not only a design but something which also focuses on the user interface. The designer should consider all of the examples and guidance given, but shouldn't let that limit any innovation.

Happy to respond to any questions and give constant feedback.

Thank you.

-*-*-*-*-*-*-*-*-*-*-*-*-*-*-*-*-

Update, 18th Nov 2011:

1. I'm about the upload the logos so you can incorporate these into your designs.

2. A UI question of mine is how to move from a list view (e.g. Resources) to editing one of those items in the list. In the spec document I showed a popup editor for these items but I don't know if that's the best thing to do. Happy to see other ideas on this - whatever the best user experience would be.

3. On the designs in the spec document I've not included any help functionality. It would be good to include pieces of guidance on each page of the administration area to help the user - guess these could either be info panels on the pages themselves or info popups. Again, would be good to see some ideas in the designs.

Also, just to be clear, I am really looking for something that looks like a modern innovative "web app" rather than it looking like a promotional corporate web site.

Target Market(s)

Owners of businesses of all types (e.g. salons, small hotels, surgeries, etc).

Industry/Entity Type

Commercial

Requirements
Must have
• Headline image transition panel on home page.

Layout, graphic and font styles along similar lines to quillbarn.com, fellgarde.co.uk, etc.
Nice to have
• Blog feed panel on the home page.

Innovative ideas for improvements to the spec.
Should not have
• Anything which can't be practically rendered when the design is converted to HTML.

Should not be overly influenced by the layout and style in the attached spec - that should just be a guide to the content and layout of the site.

```html
<!DOCTYPE html>
<html lang="en">
<head>
<meta charset="utf-8">
<title>Slotwise – Online Booking for Business</title>
<link rel="stylesheet" href="https://fonts.googleapis.com/css2?family=Source+Sans+3:wght@400;600;700&family=Noto+Sans:wght@400;700&display=swap">
<style>
:root{
  --ink:#323b3a;
  --text:#2b2f2f;
  --blue:#12b5d4;
  --blue-mid:#1aa4c4;
  --blue-deep:#0c7690;
  --footer:#0b6a80;
  --footer-link:#8fcfdd;
  --line:#bfe6ef;
  --grey-soft:#f3f4f4;
  --white:#ffffff;
}
*{box-sizing:border-box;margin:0;padding:0}
html,body{width:1200px;height:878px;overflow:hidden;background:var(--white)}
body{font-family:"Noto Sans",Tahoma,sans-serif;color:var(--text);position:relative}
.page{position:relative;width:1200px;height:878px;overflow:hidden;
  background:linear-gradient(#f5fbfd 0,#ffffff 60px)}
.abs{position:absolute}

/* header */
.brand{left:124px;top:88px;font-family:"Source Sans 3",sans-serif;font-weight:600;font-size:27px;letter-spacing:3px;color:var(--ink);display:flex;align-items:center;gap:10px}
.brand-mark{width:14px;height:14px;background:var(--blue)}
.login-title{left:521px;top:34px;font-size:11px;color:#444}
.field{top:54px;width:132px;height:27px;border:1px solid #c9e9f1;border-radius:3px;background:#fff;font-size:11px;color:#b8c4c6;padding:6px 9px}
.field-user{left:520px}
.field-pass{left:658px}
.login-btn{left:799px;top:54px;width:59px;height:27px;border-radius:3px;background:linear-gradient(#26bfdc,#0f9dbd);color:#fff;font-size:12px;text-align:center;line-height:27px}
.divider-v{left:872px;top:59px;width:1px;height:18px;background:#d8e3e6}
.flag{left:914px;top:61px;width:20px;height:14px;background:#2a4c8c;border:1px solid #b8c2d4}
.lang{left:940px;top:61px;font-size:11.5px;color:#333}
.lang-caret{left:1062px;top:64px}

.main-nav{left:348px;top:94px;width:732px;height:42px;border-radius:3px;background:linear-gradient(#25bddb,#1098b8);display:flex;overflow:hidden}
.main-nav a{display:block;height:42px;line-height:42px;color:#fff;text-decoration:none;font-weight:700;font-size:12px;text-align:center}
.main-nav .active{background:var(--blue-deep)}

/* hero */
.hero-band{left:0;top:140px;width:1200px;height:346px;background:linear-gradient(#ffffff 60%,#f1f2f2 100%)}
.hero-title{left:120px;top:186px;font-family:"Source Sans 3",sans-serif;font-weight:600;font-size:27.5px;line-height:33px;color:var(--ink)}
.hero-title em{font-style:normal;color:var(--blue)}
.hero-copy{left:120px;top:261px;width:440px;font-size:12.4px;line-height:14.6px;color:#222}
.signup{left:120px;top:358px;width:124px;height:37px;border-radius:3px;background:linear-gradient(#26b8d6,#0d86a6);color:#fff;font-family:"Source Sans 3",sans-serif;font-size:20px;text-align:center;line-height:36px}
.hero-visual{left:598px;top:166px;width:484px;height:264px;border-radius:10px 10px 4px 4px;background:linear-gradient(#e9eef0 0,#e9eef0 55%,#1b9ab6 56%,#0d7d98 92%,#c9cdcf 93%,#e6e8e9 100%)}
.slider-dots{left:538px;top:457px;display:flex;gap:20px}
.slider-dots span{width:10px;height:10px;border-radius:50%;background:#555}
.slider-dots .current{background:var(--blue-deep)}

/* body */
.section-title{font-size:16.5px;color:var(--blue-mid)}
.avail-title{left:121px;top:517px}
.avail-copy{left:120px;top:544px;width:590px;font-size:12.4px;line-height:14.6px;color:#222}
.features{left:120px;top:611px;list-style:none;font-size:12.4px;color:#222}
.features li{height:20px;display:flex;align-items:center;gap:8px}
.features li::before{content:"";border-left:5px solid var(--blue);border-top:3.5px solid transparent;border-bottom:3.5px solid transparent}
.column-shade{left:746px;top:490px;width:12px;height:260px;background:linear-gradient(90deg,rgba(0,0,0,.04),rgba(0,0,0,0))}
.news-title{left:778px;top:514px;font-size:18.5px}
.news{left:779px;width:303px;font-size:12.2px;line-height:14px;color:#222}
.news h3{font-size:12.6px;font-weight:700;color:var(--ink)}
.news-1{top:555px;padding-bottom:14px;border-bottom:1px dotted #c8d2d4}
.news-2{top:625px}
.view-more{left:779px;top:686px;font-size:11.5px;color:var(--blue-mid);text-decoration:underline}

/* footer */
.footer{left:0;top:765px;width:1200px;height:113px;background:var(--footer)}
.footer-nav{left:122px;top:797px;display:flex;align-items:center;font-size:12.4px}
.footer-nav a{color:var(--footer-link);text-decoration:none}
.footer-nav a.active{color:#fff}
.footer-nav i{width:4px;height:4px;border-radius:50%;background:var(--blue);margin:0 10px}
.copyright{left:122px;top:819px;font-size:11px;color:#6fb3c4}
.follow{left:866px;top:801px;font-size:12.5px;font-weight:700;color:#fff}
.social{left:949px;top:797px;display:flex;gap:6px}
.social span{width:24px;height:24px;border-radius:3px;background:#5fb0c8}
</style>
</head>
<body>
<div class="page">

  <header>
    <div class="abs brand"><span class="brand-mark"></span>SLOTWISE</div>
    <div class="abs login-title">Login to Slotwise</div>
    <div class="abs field field-user">Username</div>
    <div class="abs field field-pass">Password</div>
    <div class="abs login-btn">Login</div>
    <div class="abs divider-v"></div>
    <div class="abs flag" role="img" aria-label="Language flag"></div>
    <div class="abs lang">United State - English</div>
    <svg class="abs lang-caret" width="11" height="11" viewBox="0 0 11 11" aria-hidden="true">
      <circle cx="5.5" cy="5.5" r="5.5" fill="#12b5d4"/>
      <path d="M3 4.2h5L5.5 7.4z" fill="#fff"/>
    </svg>
    <nav class="abs main-nav">
      <a class="active" style="width:138px">HOME</a>
      <a style="width:164px">FEATURES</a>
      <a style="width:96px">PRICING</a>
      <a style="width:192px">SERVICES</a>
      <a style="width:80px">CONTACT US</a>
    </nav>
  </header>

  <section class="hero">
    <div class="abs hero-band"></div>
    <h1 class="abs hero-title">Save <em>50%</em> for Gold Account<br>at December 2012</h1>
    <p class="abs hero-copy">Ut wisi enim ad minim veniam, quis nostrud exerci tation ullamcorper suscipit lobortis nisl ut aliquip ex ea commodo consequat. Lorem ipsum dolor sit amet, consectetuer adipiscing elit, sed diam nonummy nibh euismod tincidunt ut laoreet dolore magna aliquam erat volutpat.</p>
    <div class="abs signup">Sign up</div>
    <div class="abs hero-visual" role="img" aria-label="Laptop showing the Gold Account offer at $19.99 per month"></div>
    <div class="abs slider-dots"><span class="current"></span><span></span><span></span><span></span></div>
  </section>

  <main>
    <h2 class="abs section-title avail-title">Make your self available</h2>
    <p class="abs avail-copy">Lorem ipsum dolor sit amet, consectetuer adipiscing elit, sed diam nonummy nibh euismod tincidunt ut laoreet dolore magna aliquam erat volutpat. Ut wisi enim ad minim veniam, quis nostrud exerci tation ullamcorper suscipit lobortis nisl ut aliquip ex ea commodo consequat.</p>
    <ul class="abs features">
      <li>Lorem ipsum dolor sit amet, consectetuer adipiscing elit.</li>
      <li>Accumsan et iusto odio dignissim qui blandit</li>
      <li>Ut wisi enim ad minim veniam</li>
      <li>Vulputate velit esse molestie consequat</li>
    </ul>

    <div class="abs column-shade"></div>
    <h2 class="abs section-title news-title">What’s Happening ?</h2>
    <article class="abs news news-1">
      <h3>Save 50% or more with Flash Deals</h3>
      <p>Lorem ipsum dolor sit amet, consectetuer adipiscing elit, sed diam nonummy nibh.</p>
    </article>
    <article class="abs news news-2">
      <h3>Booking on your smartphone</h3>
      <p>ulputate velit esse molestie consequat, vel illum dolore eu</p>
    </article>
    <a class="abs view-more">View more</a>
  </main>

  <footer>
    <div class="abs footer"></div>
    <nav class="abs footer-nav">
      <a class="active">Home</a><i></i><a>Work</a><i></i><a>Blog</a><i></i><a>Products</a><i></i><a>Services</a><i></i><a>Support</a><i></i><a>About</a><i></i><a>Contact us</a>
    </nav>
    <div class="abs copyright">Copyright © 2011 Slotwise. All right reserved.</div>
    <div class="abs follow">Follow Us</div>
    <div class="abs social" aria-label="Social links"><span></span><span></span><span></span><span></span></div>
  </footer>

</div>
</body>
</html>
```